We Are Corvale Marketing Collateral

We Are Corvale has undergone a rebrand with new logo, website, and intranet design builds. The business is now looking to update its marketing collateral with the new logo design and colour palette. Deliverables include PowerPoint template, Report template, Letterhead, and Email signature. Refer attached design brief for more information. Also attached are the logo and brand document.
Target Market(s)
Executive & Board of SME impact organisations.
Industry/Entity Type
We serve small to medium organisations who are delivering impact, not-for-profits, social enterprises and purpose driven organisations.
Font styles to use
Other font styles liked:
- Roca Two Thin, Rubik Regular
Look and feel
Each slider illustrates characteristics of the customer's brand and the style your logo design should communicate.

```html
<!DOCTYPE html>
<html lang="en">
<head>
<meta charset="utf-8">
<title>We Are Corvale – Collateral Suite</title>
<link rel="stylesheet" href="https://fonts.googleapis.com/css2?family=Rubik:wght@300;400;500;700&family=Zilla+Slab:wght@400;700&family=Oswald:wght@500&display=swap">
<style>
:root{
  --bg:#2a2a2a;
  --paper:#ffffff;
  --ink:#17504a;
  --ink-soft:#5b6d6a;
  --teal:#2a9aa8;
  --green:#3aaa6a;
  --pink:#c8407a;
  --red:#e8505b;
  --orange:#f08a3c;
  --label:#e6e6e6;
  --dots:linear-gradient(135deg,var(--green) 0%,var(--teal) 25%,var(--pink) 50%,var(--red) 70%,var(--orange) 100%);
}
*{box-sizing:border-box;margin:0;padding:0}
html,body{width:1200px;height:602px;overflow:hidden;background:var(--bg)}
body{font-family:"Rubik",sans-serif;color:var(--ink)}
.board{position:relative;width:1200px;height:602px}
.section-label{position:absolute;font-size:6.3px;color:var(--label);font-weight:300}
.sheet{position:absolute;background:var(--paper);overflow:hidden;box-shadow:0 2px 6px rgba(0,0,0,.45)}
.abs{position:absolute}
.dot-field{position:absolute;background:var(--dots);opacity:.85;border-radius:50% 50% 0 50%}
.photo{position:absolute;background:linear-gradient(135deg,#c9d3d6,#8b9a9c 60%,#5e6b6c)}
.brand{position:absolute;display:flex;align-items:center;gap:.35em;color:var(--ink);font-weight:400;letter-spacing:.04em}
.brand-dot{width:1.1em;height:1.1em;border-radius:50%;background:var(--teal);flex:none}
.contact{position:absolute;color:var(--ink-soft);font-weight:300;line-height:1.55}
.contact span{display:flex;align-items:center;gap:.35em}
.contact i{width:.8em;height:.8em;border-radius:50%;background:var(--ink);display:inline-block}
.para{position:absolute;color:var(--ink-soft);font-weight:300;line-height:1.35}
.slide-foot{position:absolute;left:7px;right:9px;bottom:8px;height:6px;display:flex;align-items:flex-end;gap:1px;font-size:6px;color:var(--teal);letter-spacing:.04em}
.slide-foot b{flex:1;height:1px;background:var(--ink);margin-bottom:1px;font-weight:400}
.slide-foot em{width:5px;height:5px;border-radius:50%;background:var(--ink);font-style:normal}
.checks{position:absolute;list-style:none;color:var(--ink-soft);font-weight:300}
.checks li::before{content:"✓ ";color:var(--ink)}
</style>
</head>
<body>
<main class="board">

  <p class="section-label" style="left:51px;top:67px">Email signature</p>
  <p class="section-label" style="left:318px;top:67px">Letterhead</p>
  <p class="section-label" style="left:647px;top:67px">PowerPoint Template</p>
  <p class="section-label" style="left:51px;top:155px">Report Templatee</p>

  <!-- Email signature -->
  <section class="sheet email-signature" style="left:51px;top:81px;width:253px;height:64px">
    <div class="brand" style="left:8px;top:25px;font-size:10px"><span class="brand-dot"></span>CORVALE</div>
    <div class="abs" style="left:81px;top:14px;width:.5px;height:38px;background:var(--ink)"></div>
    <div class="abs" style="left:84px;top:16px;font-size:7px;font-weight:500">MARA ELLISON</div>
    <div class="abs" style="left:84px;top:24px;font-size:4.3px;color:var(--ink-soft)">Manager</div>
    <div class="contact" style="left:84px;top:31px;font-size:3.8px">
      <span><i></i>(+61) 140 552 918</span>
      <span><i></i>hello@corvale-mail.org</span>
      <span><i></i>www.corvale-impact.org</span>
    </div>
    <div class="dot-field" role="img" aria-label="Cluster of coloured dots" style="left:160px;top:27px;width:92px;height:37px"></div>
  </section>

  <!-- Report -->
  <section class="sheet report" style="left:51px;top:166px;width:254px;height:356px">
    <div class="brand" style="left:15px;top:20px;font-size:13px"><span class="brand-dot"></span>CORVALE</div>
    <div class="abs" style="right:10px;top:13px;text-align:right">
      <div style="font-size:11px;font-weight:300;color:var(--teal)">HEADLINE</div>
      <div style="font-size:11.5px;font-weight:500;margin-top:1px">LOREM IPSUM</div>
      <div style="width:50px;height:1px;background:var(--ink);margin:3px 0 2px auto"></div>
      <div style="font-size:4.6px;letter-spacing:.25em;font-weight:500">SPACE HERE</div>
    </div>
    <div class="abs" style="left:17px;top:78px;font-family:'Oswald',sans-serif;font-size:30px;font-weight:500;line-height:1">2022</div>
    <div class="abs" style="left:17px;top:113px;font-size:21px;font-weight:400;line-height:1">AMMUAL</div>
    <div class="abs" style="left:16px;top:137px;font-size:24px;font-weight:700;line-height:1">REPORT</div>
    <div class="abs" style="left:17px;top:164px;width:70px;height:1.2px;background:var(--ink)"></div>
    <div class="abs" style="left:17px;top:171px;font-size:7px;font-weight:500">Lorem ipsum dolor sit amet</div>
    <p class="para" style="left:17px;top:182px;width:116px;font-size:4.9px">Lorem ipsum dolor sit amet, consectetuer adipiscing elit, sed diam nonummy nibh euis-mod tincidunt ut laoreet dolore magna aliquam erat volutpat. Ut wisi enim ad</p>
    <div class="abs" style="left:15px;top:245px;font-size:8px;font-weight:500">Lorem Ipsum Dolor</div>
    <ul class="checks" style="left:15px;top:258px;font-size:4.8px;line-height:8.2px">
      <li>Lorem ipsum dolor sit amet nonummy</li>
      <li>Consectetuer adipiscing elit sed dolor sit</li>
      <li>Diam nonummy nibh euismod ipsum dolor</li>
      <li>Lorem ipsum dolor sit amet adipiscing elit</li>
      <li>Consectetuer adipiscing elit sed nibh</li>
      <li>Diam nonummy nibh euismod</li>
    </ul>
    <div class="abs" style="left:15px;top:333px;font-size:6.3px;font-weight:700;letter-spacing:.12em">WWW.CORVALE-IMPACT.ORG</div>
    <div class="dot-field" role="img" aria-label="Large arc of coloured dots" style="left:138px;top:92px;width:116px;height:264px;border-radius:100% 0 0 100%"></div>
  </section>

  <!-- Letterhead -->
  <section class="sheet letterhead" style="left:318px;top:82px;width:314px;height:440px">
    <div class="brand" style="left:11px;top:15px;font-size:13px"><span class="brand-dot"></span>CORVALE</div>
    <div class="contact" style="left:14px;top:402px;font-size:5.8px">
      <span><i></i>(+61) 140 552 918</span>
      <span><i></i>hello@corvale-mail.org</span>
      <span><i></i>www.corvale-impact.org</span>
    </div>
    <div class="dot-field" role="img" aria-label="Cluster of coloured dots" style="left:167px;top:383px;width:147px;height:57px"></div>
  </section>

  <!-- Slide 1: cover -->
  <section class="sheet slide" style="left:647px;top:82px;width:246px;height:138px">
    <div class="abs" style="left:11px;top:10px;font-family:'Zilla Slab',serif;font-size:17px;line-height:1">Company</div>
    <div class="abs" style="left:11px;top:32px;font-family:'Zilla Slab',serif;font-weight:700;font-size:19px;line-height:1">Presentation</div>
    <div class="abs" style="left:11px;top:56px;font-weight:700;font-size:21px;line-height:1">2022</div>
    <div class="abs" style="left:11px;top:82px;width:60px;height:1.2px;background:var(--ink)"></div>
    <div class="abs" style="left:11px;top:88px;font-size:6px;font-weight:500">Lorem ipsum dolor sit amet</div>
    <p class="para" style="left:11px;top:97px;width:92px;font-size:3.4px">Lorem ipsum dolor sit amet, consectetuer adipiscing elit, sed diam nonummy nibh euismod tincidunt ut laoreet dolore magna aliquam erat volutpat. Ut wisi enim ad</p>
    <div class="abs" style="left:11px;top:126px;font-size:4.4px;font-weight:700;letter-spacing:.1em">WWW.CORVALE-IMPACT.ORG</div>
    <div class="brand" style="left:171px;top:18px;font-size:10px"><span class="brand-dot"></span>CORVALE</div>
    <div class="dot-field" role="img" aria-label="Burst of coloured dots" style="left:107px;top:74px;width:139px;height:64px;border-radius:100% 100% 0 0"></div>
  </section>

  <!-- Slide 2: contents -->
  <section class="sheet slide" style="left:903px;top:82px;width:246px;height:138px">
    <div class="abs" style="left:22px;top:20px;font-size:14px;font-weight:700">Contents</div>
    <div class="abs" style="left:22px;top:38px;width:60px;height:1.2px;background:var(--ink)"></div>
    <div class="abs" style="left:22px;top:46px;font-size:5.8px;font-weight:500">1.&nbsp; Lorem ipsum</div>
    <p class="para" style="left:30px;top:53px;width:92px;font-size:3.2px">Lorem ipsum dolor sit amet, consectetuer adipiscing elit, sed diam nonummy nibh euismod tincid</p>
    <div class="abs" style="left:22px;top:73px;font-size:5.8px;font-weight:500">2.&nbsp; Lorem ipsum</div>
    <p class="para" style="left:30px;top:80px;width:92px;font-size:3.2px">Lorem ipsum dolor sit amet, consectetuer adipiscing elit, sed diam nonummy nibh euismod tincid</p>
    <div class="abs" style="left:22px;top:98px;font-size:5.8px;font-weight:500">3.&nbsp; Lorem ipsum</div>
    <p class="para" style="left:30px;top:105px;width:92px;font-size:3.2px">Lorem ipsum dolor sit amet, consectetuer adipiscing elit, sed diam nonummy nibh euismod tincid</p>
    <div class="dot-field" role="img" aria-label="Ring of coloured dots" style="left:138px;top:29px;width:84px;height:84px;border-radius:50%"></div>
    <div class="slide-foot">CORVALE<b></b><em></em></div>
  </section>

  <!-- Slide 3: domain -->
  <section class="sheet slide" style="left:647px;top:232px;width:246px;height:139px">
    <div class="dot-field" role="img" aria-label="Ring of coloured dots" style="left:26px;top:28px;width:84px;height:84px;border-radius:50%"></div>
    <div class="photo" role="img" aria-label="Photo of a team meeting in an office" style="left:44px;top:46px;width:48px;height:48px;border-radius:50%"></div>
    <div class="abs" style="left:120px;top:30px;font-size:6.5px;line-height:1.2">WHAT'S A DOMAIN?<br>IT'S THAT NAME UP<br><b style="font-weight:500">IN THE ADDRESS BAR.</b></div>
    <ul class="checks" style="left:120px;top:62px;font-size:3.6px;line-height:8.8px">
      <li>Fits your business or products and remember</li>
      <li>Is easy to spell and rememberor products</li>
      <li>Fits your business or products and remember</li>
      <li>Is easy to spell and remember easy to spell</li>
      <li>Fits your business or products spell and rememberor</li>
      <li>Is easy to spell and remember business or products</li>
    </ul>
    <div class="slide-foot">CORVALE<b></b><em></em></div>
  </section>

  <!-- Slide 4: market -->
  <section class="sheet slide" style="left:903px;top:232px;width:246px;height:139px">
    <div class="dot-field" role="img" aria-label="Cluster of coloured dots" style="left:0;top:0;width:68px;height:34px;border-radius:0 0 50% 50%"></div>
    <div class="abs" style="left:12px;top:42px;font-size:9px;line-height:1.05">MARKET<br><b style="font-weight:500">OPPORTUNITIES</b></div>
    <p class="para" style="left:12px;top:69px;width:106px;font-size:3.1px">Lorem ipsum dolor sit amet, consectetuer adipiscing elit, sed diam nonummy nibh euismod tincidunt ut laoreet dolore magna aliquam erat volutpat. Ut wisi enim ad minim veniam, quis nostrud exerci tation ullamcorper suscipit lobortis nisl ut aliquip ex ea commodo consequat.</p>
    <p class="para" style="left:12px;top:95px;width:106px;font-size:3.1px">Lorem ipsum dolor sit amet, consectetuer adipiscing elit, sed diam nonummy nibh euismod tincidunt ut laoreet dolore magna aliquam erat volutpat. Ut wisi enim ad minim veniam, quis nostrud exerci tation ullamcorper suscipit lobortis nisl ut aliquip ex ea commodo consequat.</p>
    <svg class="abs" style="left:144px;top:18px" width="90" height="56" viewBox="0 0 90 56">
      <g stroke="#e2e2e2" stroke-width=".3">
        <path d="M4 4H88M4 12H88M4 20H88M4 28H88M4 36H88M4 44H88M4 52H88"/>
        <path d="M12 4V52M20 4V52M28 4V52M36 4V52M44 4V52M52 4V52M60 4V52M68 4V52M76 4V52M84 4V52"/>
      </g>
      <g fill="none" stroke-width=".8">
        <path d="M5 50C15 20 30 14 60 12S80 20 86 10" stroke="var(--green)"/>
        <path d="M5 50C18 28 30 22 50 22S70 30 86 12" stroke="var(--red)"/>
        <path d="M5 50C20 34 40 28 60 32S78 36 86 26" stroke="var(--teal)"/>
        <path d="M5 50C20 40 40 30 56 36S74 44 86 38" stroke="var(--pink)"/>
        <path d="M5 50C25 44 45 44 62 46S76 18 86 12" stroke="var(--orange)"/>
      </g>
      <rect x="22" y="1" width="20" height="6" fill="var(--green)"/>
      <text x="32" y="5.2" font-size="2.6" fill="#fff" text-anchor="middle" font-family="Rubik,sans-serif">TEXT HERE</text>
    </svg>
    <svg class="abs" style="left:148px;top:80px" width="86" height="40" viewBox="0 0 86 40">
      <path d="M4 2V37H86" stroke="#ccc" stroke-width=".4" fill="none"/>
      <path d="M6 37C10 30 14 28 18 34S26 32 32 26S40 34 46 32S52 24 58 10S68 30 74 34S80 36 84 37Z" fill="var(--ink)"/>
      <g font-size="2.6" font-family="Rubik,sans-serif" text-anchor="middle">
        <text x="12" y="22" fill="var(--green)">100</text>
        <text x="22" y="28" fill="var(--orange)">20</text>
        <text x="36" y="16" fill="var(--teal)">275</text>
        <text x="48" y="22" fill="var(--pink)">130</text>
        <text x="60" y="6" fill="var(--orange)">650</text>
        <text x="80" y="25" fill="var(--green)">80</text>
      </g>
    </svg>
    <div class="slide-foot">CORVALE<b></b><em></em></div>
  </section>

  <!-- Slide 5: advantage -->
  <section class="sheet slide" style="left:647px;top:383px;width:246px;height:138px">
    <div class="dot-field" role="img" aria-label="Cluster of coloured dots" style="left:10px;top:14px;width:70px;height:82px;border-radius:50%"></div>
    <div class="photo" role="img" aria-label="Photo of colleagues working together at a laptop" style="left:31px;top:32px;width:83px;height:80px;background:linear-gradient(135deg,#e9eef0,#a6b4bd 55%,#3f5a78)"></div>
    <div class="abs" style="left:122px;top:26px;font-size:10px;line-height:1.1">COMPANY<br><b style="font-weight:500">ADVANTAGE</b></div>
    <div class="abs" style="left:122px;top:50px;width:40px;height:1px;background:var(--ink)"></div>
    <p class="para" style="left:122px;top:54px;width:105px;font-size:3.3px">Lorem ipsum dolor sit amet, consectetuer adipiscing elit, sed diam nonummy nibh euismod tincidunt ut laoreet dolore magna aliquam erat volutpat. Ut wisi enim ad minim veniam, quis nostrud exerci tation ullam</p>
    <p class="para" style="left:122px;top:75px;width:105px;font-size:3.3px">Lorem ipsum dolor sit amet, consectetuer adipiscing elit, sed diam nonummy nibh euismod tincidunt ut laoreet dolore magna aliquam erat volutpat. Ut wisi enim ad minim veniam, quis nostrud exerci tation ullam</p>
    <p class="para" style="left:122px;top:96px;width:105px;font-size:3.3px">Lorem ipsum dolor sit amet, consectetuer adipiscing elit, sed diam nonummy nibh euismod tincidunt ut laoreet dolore magna aliquam erat volutpat. Ut wisi enim ad minim veniam, quis nostrud exerci</p>
    <div class="slide-foot">CORVALE<b></b><em></em></div>
  </section>

  <!-- Slide 6: thank you -->
  <section class="sheet slide" style="left:903px;top:383px;width:246px;height:138px">
    <div class="brand" style="left:15px;top:22px;font-size:15px"><span class="brand-dot"></span>CORVALE</div>
    <div class="abs" style="left:15px;top:74px;font-size:14px;font-weight:500">Thank You</div>
    <div class="abs" style="left:15px;top:93px;width:36px;height:1px;background:var(--ink)"></div>
    <div class="contact" style="left:15px;top:98px;font-size:5px">
      <span><i></i>(+61) 140 552 918</span>
      <span><i></i>hello@corvale-mail.org</span>
      <span><i></i>www.corvale-impact.org</span>
    </div>
    <div class="dot-field" role="img" aria-label="Large burst of coloured dots" style="left:120px;top:25px;width:126px;height:113px;border-radius:100% 0 0 0"></div>
  </section>

</main>
</body>
</html>
```